Custom Real Estate Postcard for Buying Communities

We are a real estate company that owns/operates mobile home parks and want to send out a postcard to owners of these communities letting them know who our company is and let them know we want to buy their community. We are looking to create a postcard that introduces our company to the owner and also lets them know we want to buy their community - we are targeting older mom & pop type communities so we would like the postcard to have a home-y feel that makes the owner feel like our company will treat them fairly during the acquisition process
I have attached a few images from our communities that might look good on a postcard - you don't need to use all of them, I just included multiple so there are different options. please feel free to edit/enhance the images if needed.
Our company is Bright Meadow Holdings (BMH) and the logo is attached.
Text to be included somewhere on postcard: "We pride ourselves on active hands-on management in order to provide our residents quality communities at an affordable price.
BMH is a proven owner/operator and has the ability to purchase without any financing contingencies.
We provide a quick and easy closing. We do not retrade
Target Market(s)
Owners of Mobile Home Parks that BMH (our company) would like to acquire - small mom & pop owners that want to see that we aren't the big firm trying to come in and take over but a local company that will still treat the residents well
Industry/Entity Type
Real Estate
Colors
Designer to choose colors to be used in the design.
Requirements
Must have
- The BMH logo, at least one picture of a mobile home park from the attached pictures. And some version/form of the provided text. Info/contact section with website (www.bmhparks.example), email (info@bmhparks.example) and phone (555.284.7160)
- Something sort of call to action like: "We Want to Buy Your Community", "Ready to Sell?", "Interested in Selling?" etc.
Nice to have
- BMH Logo Colors, in addition to any other colors if designer thinks there are complimentary colors

```html
<!DOCTYPE html>
<html lang="en">
<head>
<meta charset="utf-8">
<title>Bright Meadow Holdings Postcard</title>
<link rel="stylesheet" href="https://fonts.googleapis.com/css2?family=Montserrat:wght@400;500;600&display=swap">
<style>
  :root {
    --backdrop: #e9e6e1;
    --paper: #ffffff;
    --brick: #8e2f1f;
    --slate: #3f3f41;
    --rule: #d8d8d8;
    --stamp: #e3e3e3;
  }
  * { box-sizing: border-box; margin: 0; padding: 0; }
  html, body { width: 1200px; height: 903px; overflow: hidden; }
  body {
    background: var(--backdrop);
    font-family: "Montserrat", Arial, sans-serif;
    display: flex;
    align-items: center;
    justify-content: center;
    gap: 40px;
  }
  .postcard {
    position: relative;
    width: 555px;
    height: 375px;
    background: var(--paper);
    box-shadow: 0 6px 18px rgba(0,0,0,.18);
    overflow: hidden;
  }
  .photo { position: absolute; }

  /* front */
  .front .photo-main { left: 10px; top: 10px; width: 535px; height: 190px;
    background: linear-gradient(160deg, #7aa7d8 0%, #5e8c3c 35%, #d9d7cf 55%, #6f9a3d 100%); }
  .front .photo-street { left: 10px; top: 206px; width: 170px; height: 92px;
    background: linear-gradient(170deg, #5b9be0 0%, #4f8a34 50%, #9a9a98 100%); }
  .front .photo-home { left: 186px; top: 206px; width: 175px; height: 92px;
    background: linear-gradient(160deg, #a9cbe8 0%, #4a7d2d 45%, #d8cbb6 75%, #5c8c2f 100%); }
  .front .photo-porch { left: 367px; top: 206px; width: 178px; height: 92px;
    background: linear-gradient(170deg, #3d7fd0 0%, #e5e5e3 45%, #8b8f4c 100%); }
  .front .brand { position: absolute; left: 18px; top: 318px; }
  .front .cta-band {
    position: absolute; left: 186px; top: 304px; width: 359px; height: 61px;
    background: var(--brick); color: #fff; padding: 7px 12px;
  }
  .cta-title { font-size: 10.5px; font-weight: 600; line-height: 1.25; margin-bottom: 4px; }
  .contact-row { display: flex; gap: 10px; font-size: 8px; align-items: center; white-space: nowrap; }
  .contact-row span { display: inline-flex; align-items: center; gap: 4px; flex: none; }
  .contact-row svg { width: 9px; height: 9px; flex: none; }

  .brand { display: flex; align-items: center; gap: 8px; }
  .brand-mark { width: 14px; height: 14px; background: var(--brick); flex: none; }
  .brand-name {
    font-size: 12px; font-weight: 600; color: var(--brick);
    text-transform: uppercase; line-height: 1.1; letter-spacing: .5px;
  }

  /* back */
  .back .intro-panel {
    position: absolute; left: 0; top: 0; width: 330px; height: 125px;
    background: var(--brick); color: #fff; padding: 16px 16px;
    font-size: 9.3px; line-height: 1.5;
  }
  .back .photo-aerial { left: 0; top: 125px; width: 330px; height: 180px;
    background: linear-gradient(150deg, #4c7b3a 0%, #7fa35a 40%, #a9ab9e 60%, #5f8a3e 100%); }
  .back .contact-bar {
    position: absolute; left: 0; top: 305px; width: 330px; height: 70px;
    background: var(--slate); color: #fff; padding: 12px 10px;
  }
  .back .contact-bar .cta-title { font-size: 9.5px; margin-bottom: 6px; }
  .back .contact-bar .contact-row { font-size: 7.5px; gap: 8px; }
  .back .address-side { position: absolute; left: 330px; top: 0; width: 225px; height: 375px; }
  .back .address-side .brand { position: absolute; left: 18px; top: 62px; }
  .back .address-side .brand-name { font-size: 10px; }
  .stamp-box { position: absolute; right: 16px; top: 18px; width: 52px; height: 52px; background: var(--stamp); }
  .address-line { position: absolute; left: 25px; width: 180px; height: 1px; background: var(--rule); }
  .address-line.l1 { top: 175px; }
  .address-line.l2 { top: 210px; }
  .address-line.l3 { top: 245px; }
  .footer-stripe { position: absolute; left: 0; bottom: 0; width: 225px; height: 8px; background: var(--brick); }
</style>
</head>
<body>

<svg width="0" height="0" style="position:absolute" aria-hidden="true">
  <symbol id="icon-phone" viewBox="0 0 12 12">
    <circle cx="6" cy="6" r="5.4" fill="none" stroke="currentColor" stroke-width="1"/>
    <path d="M4.2 3.5c.3-.3.7-.3.9 0l.5.7c.2.3.1.6-.1.8l-.3.3c.3.6.8 1.1 1.4 1.4l.3-.3c.2-.2.5-.3.8-.1l.7.5c.3.2.3.6 0 .9-.8.8-2 .5-3.1-.6S3.4 4.3 4.2 3.5z" fill="currentColor"/>
  </symbol>
  <symbol id="icon-mail" viewBox="0 0 12 12">
    <circle cx="6" cy="6" r="5.4" fill="none" stroke="currentColor" stroke-width="1"/>
    <rect x="3.3" y="4.2" width="5.4" height="3.6" fill="none" stroke="currentColor" stroke-width=".8"/>
    <path d="M3.3 4.2 6 6.3l2.7-2.1" fill="none" stroke="currentColor" stroke-width=".8"/>
  </symbol>
  <symbol id="icon-web" viewBox="0 0 12 12">
    <circle cx="6" cy="6" r="5.4" fill="none" stroke="currentColor" stroke-width="1"/>
    <circle cx="6" cy="6" r="2.8" fill="none" stroke="currentColor" stroke-width=".8"/>
    <path d="M3.2 6h5.6M6 3.2v5.6" stroke="currentColor" stroke-width=".6"/>
  </symbol>
</svg>

<article class="postcard front">
  <div class="photo photo-main" role="img" aria-label="Photo of a white manufactured home with green shutters, deck and flowering shrubs"></div>
  <div class="photo photo-street" role="img" aria-label="Photo of a tree-lined street in a home community"></div>
  <div class="photo photo-home" role="img" aria-label="Photo of a beige manufactured home among trees"></div>
  <div class="photo photo-porch" role="img" aria-label="Photo of a home with a white porch and landscaped yard"></div>

  <div class="brand">
    <span class="brand-mark"></span>
    <span class="brand-name">Bright Meadow<br>Holdings</span>
  </div>

  <div class="cta-band">
    <p class="cta-title">Please contact us if you are interested in selling your community</p>
    <div class="contact-row">
      <span><svg><use href="#icon-phone"/></svg>555.284.7160</span>
      <span><svg><use href="#icon-mail"/></svg>info@bmhparks.example</span>
      <span><svg><use href="#icon-web"/></svg>www.bmhparks.example</span>
    </div>
  </div>
</article>

<article class="postcard back">
  <div class="intro-panel">
    <p>Bright Meadow Holdings (BMH) is among the fastest-growing companies in the Manufactured Housing Industry and is constantly looking for communities to acquire. BMH has significant capital resources and the ability to make acquisitions without financing contingencies. We offer a quick due diligence and closing time line and we do not retrade.</p>
  </div>
  <div class="photo photo-aerial" role="img" aria-label="Aerial photo of a manufactured home community surrounded by green fields and woods"></div>
  <div class="contact-bar">
    <p class="cta-title">Please contact us if you are interested in selling your community</p>
    <div class="contact-row">
      <span><svg><use href="#icon-phone"/></svg>555.284.7160</span>
      <span><svg><use href="#icon-mail"/></svg>info@bmhparks.example</span>
      <span><svg><use href="#icon-web"/></svg>www.bmhparks.example</span>
    </div>
  </div>

  <div class="address-side">
    <div class="stamp-box"></div>
    <div class="brand">
      <span class="brand-mark"></span>
      <span class="brand-name">Bright Meadow<br>Holdings</span>
    </div>
    <div class="address-line l1"></div>
    <div class="address-line l2"></div>
    <div class="address-line l3"></div>
    <div class="footer-stripe"></div>
  </div>
</article>

</body>
</html>
```